A property investment company, looking to provide lovely sustainable homes for familys and individua

For a small investment business i am starting which will buy and refurbish unloved houses and apartments to rent out or resell. the company name is my family surname (HARGREAVE). <br/>i would like the design to be simple with maybe some emphasis on an ethical and sustainable/environmentally friendly approach with a branding of maybe trees blended with some houses and or apartments.<br/>The colours i like for this design would be mainly green on either a white or black background.
Target Market(s)
This business card is to be used for professional people such as estate agents
mortgage brokers, solicitors and trades people.
Industry/Entity Type
Real Estate
Contact Information for Business Card
owner/director-Martin hargreave
e-mail-martin@hwlettings.co.uk
website-hargreavehomeholdings.co.uk
mobile-07934560218
landline-02086543107

```html
<!DOCTYPE html>
<html lang="en">
<head>
<meta charset="utf-8">
<title>Hargreave — Business Cards</title>
<link rel="stylesheet" href="https://fonts.googleapis.com/css2?family=Lato:wght@400;700&display=swap">
<style>
  :root {
    --stage: #eef0ef;
    --card-white: #ffffff;
    --card-black: #000000;
    --brand-green: #9bcb3c;
    --brand-teal: #33b8a6;
    --ink: #2b2b2b;
    --ink-soft: #555555;
  }
  * { box-sizing: border-box; margin: 0; padding: 0; }
  html, body {
    width: 1200px; height: 899px; overflow: hidden;
    background: var(--stage);
    font-family: "Lato", Arial, sans-serif;
  }
  .stage {
    position: relative; width: 1200px; height: 899px;
  }
  .card {
    position: absolute; top: 305px;
    width: 510px; height: 290px;
    box-shadow: 0 10px 28px rgba(0,0,0,0.12);
  }
  .card--back { left: 60px; background: var(--card-black); }
  .card--front { left: 630px; background: var(--card-white); }

  .brand {
    position: absolute;
    display: flex; align-items: center; gap: 12px;
  }
  .brand__square {
    width: 26px; height: 26px; background: var(--brand-teal);
  }
  .brand__name {
    font-weight: 700; color: var(--brand-green);
    letter-spacing: 0.04em; line-height: 1;
  }
  .card--back .brand { right: 48px; bottom: 48px; }
  .card--back .brand__name { font-size: 40px; }
  .card--front .brand { left: 40px; top: 40px; }
  .card--front .brand__name { font-size: 30px; }
  .card--front .brand__square { width: 20px; height: 20px; }

  .contact {
    position: absolute; right: 36px; top: 128px;
    text-align: right; color: var(--ink);
  }
  .contact__name { font-weight: 700; font-size: 22px; }
  .contact__role { font-size: 17px; color: var(--ink-soft); margin-bottom: 14px; }
  .contact__line { font-size: 15px; font-weight: 700; line-height: 1.4; }
  .contact__label { color: var(--brand-green); font-weight: 400; }
</style>
</head>
<body>
<main class="stage">
  <section class="card card--back" aria-label="Business card back">
    <div class="brand">
      <span class="brand__square"></span>
      <span class="brand__name">HARGREAVE</span>
    </div>
  </section>

  <section class="card card--front" aria-label="Business card front">
    <div class="brand">
      <span class="brand__square"></span>
      <span class="brand__name">HARGREAVE</span>
    </div>
    <div class="contact">
      <p class="contact__name">Martin Hargreave</p>
      <p class="contact__role">owner/director</p>
      <p class="contact__line"><span class="contact__label">mobile-</span>07934560218</p>
      <p class="contact__line"><span class="contact__label">landline-</span>02086543107</p>
      <p class="contact__line"><span class="contact__label">e-mail-</span>martin@hwlettings.co.uk</p>
      <p class="contact__line">hargreavehomeholdings.co.uk</p>
    </div>
  </section>
</main>
</body>
</html>
```